Quirky Business Card Design

Business card:
A quirky card for a professional audience

Business:
A professional consultancy offering corporate training and coaching

I've attached my sketches and happy for you to shapen the design and/or add your own ideas.

Front of card (see file 2 below):
Card must be easy for client to find among many
A bit quirky – implies that it needs thought, needs orientation
White card, black high gloss letters

Arrows:
One spot colour – fresh amber-orange, but not fluro nor candy colour
A colour that is not feminine nor masculine; old nor young
Meant to represent the amber of traffic lights
? black outline
Arrows oriented left to right and bottom to top i.e. headed in the right direction
May need to work in a straight line for header or footer or invoices (see file 3 below)

Back of card (e.g. in file 1):
Very clean and easy to read
Preferred fonts: I like the aesthetic of Century Gothic but with “a”.
Copy to include:
Kettle Bloom Co
Marnie Talbot
t: +61 (0)412 307 196
e: marnie@kettlebloomco.com
w: www.kettlebloomco.com

May use the by-line “Making the remarkable happen”

I am looking for a web page design in the future so I am looking to be delighted!!

Dear Designers,

I would like the copy at the back of the card to include the registered business number: 

ABN: 8123 604 2917

Many thanks,

Marnie.

Industry/Entity Type

Training

```html
<!DOCTYPE html>
<html lang="en">
<head>
<meta charset="utf-8">
<title>Kettle Bloom Co — Business Card Concepts</title>
<link rel="stylesheet" href="https://fonts.googleapis.com/css2?family=Questrial&family=Old+Standard+TT&family=Arimo&display=swap">
<style>
  :root {
    --paper: #ffffff;
    --ink: #1a1a1a;
    --amber: #e9b321;
    --card-edge: #9a9a9a;
    --sheet-edge: #c8c8c8;
    --text-font: "Questrial", "Century Gothic", sans-serif;
    --tag-font: "Old Standard TT", "Century Schoolbook", serif;
    --label-font: "Arimo", Arial, sans-serif;
  }
  * { box-sizing: border-box; margin: 0; padding: 0; }
  html, body { width: 1200px; height: 846px; overflow: hidden; background: var(--paper); }
  .sheet {
    position: relative; width: 1200px; height: 846px;
    border: 1px solid var(--sheet-edge); background: var(--paper);
    color: var(--ink); font-family: var(--text-font);
  }
  .card {
    position: absolute; width: 520px; height: 314px;
    border: 1px solid var(--card-edge); background: var(--paper);
  }
  .card--front-tagline { left: 50px;  top: 52px; }
  .card--front-plain   { left: 630px; top: 52px; }
  .card--back-text     { left: 50px;  top: 437px; }
  .card--back-logo     { left: 630px; top: 437px; }

  .side-label {
    position: absolute; font-family: var(--label-font);
    font-size: 44px; line-height: 1; color: #111; transform: translateX(-50%);
  }

  /* Wordmark: invented name in the text face, one colour, one weight, one square */
  .wordmark {
    position: absolute; left: 50%; transform: translateX(-50%);
    display: flex; align-items: center; gap: 14px; white-space: nowrap;
    font-family: var(--text-font); font-weight: 400; color: var(--ink); line-height: 1;
  }
  .wordmark__square { display: block; background: var(--amber); flex: none; }
  .wordmark--large { font-size: 44px; }
  .wordmark--large .wordmark__square { width: 30px; height: 30px; }
  .wordmark--small { font-size: 34px; gap: 11px; }
  .wordmark--small .wordmark__square { width: 23px; height: 23px; }

  .tagline {
    position: absolute; left: 146px; top: 238px; width: 241px;
    border-top: 2px solid var(--amber); border-bottom: 2px solid var(--amber);
    padding: 4px 0 6px; font-family: var(--tag-font); font-size: 15px;
    text-align: center; color: var(--ink); white-space: nowrap;
  }

  .back-details { position: absolute; left: 0; width: 100%; text-align: center; }
  .business-name { font-size: 29px; font-weight: 400; letter-spacing: 0.8px; line-height: 1; }
  .person-name { font-size: 19px; font-weight: 400; line-height: 1; letter-spacing: 0.4px; }
  .contact-list { list-style: none; font-size: 17px; letter-spacing: 1.4px; line-height: 22px; white-space: nowrap; }
  .contact-list .key { color: var(--amber); }

  .card--back-logo .rule {
    position: absolute; left: 170px; top: 179px; width: 188px;
    border-top: 1px solid var(--ink);
  }
  .card--back-logo .person-name { font-size: 22px; }
  .card--back-logo .contact-list { font-size: 15px; letter-spacing: 1px; line-height: 21px; }
</style>
</head>
<body>
<main class="sheet">

  <section class="card card--front-tagline" aria-label="Front with tagline">
    <div class="wordmark wordmark--large" style="top:112px;">
      <span class="wordmark__square"></span><span>Kettle Bloom Co</span>
    </div>
    <p class="tagline">Making the remarkable happen.</p>
  </section>
  <span class="side-label" style="left:272px; top:372px;">front</span>

  <section class="card card--front-plain" aria-label="Front, logo only">
    <div class="wordmark wordmark--large" style="top:136px;">
      <span class="wordmark__square"></span><span>Kettle Bloom Co</span>
    </div>
  </section>
  <span class="side-label" style="left:893px; top:372px;">front</span>

  <section class="card card--back-text" aria-label="Back, text only">
    <div class="back-details" style="top:72px;">
      <h1 class="business-name">Kettle Bloom Co</h1>
      <p class="person-name" style="margin-top:8px;">Marnie Talbot</p>
      <ul class="contact-list" style="margin-top:42px;">
        <li><span class="key">t:</span> +61 (0)412 307 196</li>
        <li><span class="key">e:</span> marnie@kettlebloomco.com</li>
        <li><span class="key">w:</span> www.kettlebloomco.com</li>
        <li><span class="key">ABN:</span> 8123 604 2917</li>
      </ul>
    </div>
  </section>
  <span class="side-label" style="left:310px; top:756px;">back</span>

  <section class="card card--back-logo" aria-label="Back with logo">
    <div class="wordmark wordmark--small" style="top:92px;">
      <span class="wordmark__square"></span><span>Kettle Bloom Co</span>
    </div>
    <span class="rule"></span>
    <div class="back-details" style="top:186px;">
      <p class="person-name">Marnie Talbot</p>
      <ul class="contact-list" style="margin-top:40px;">
        <li><span class="key">t:</span> +61 (0)412 307 196.<span class="key">e:</span> marnie@kettlebloomco.com</li>
        <li><span class="key">w:</span> www.kettlebloomco.com.<span class="key">ABN:</span> 8123 604 2917</li>
      </ul>
    </div>
  </section>
  <span class="side-label" style="left:890px; top:756px;">back</span>

</main>
</body>
</html>
```